Political Marketing Company - Valentine's Day Card - Huge!

We need a 5"x7" Valentine's Day card in the style of the attached images. We want it to be slightly cartoon-y, but heartfelt. Copy for card is as follows, with direction:Outside: My love for you is…(Text only, bold san-serif font, light background)Inside: HUUUUUUUGE! (graphic of Harold Benning with hands out spanning both inside pages with “HUUUUUUUUGE!” above Benning, big, bold san serif font).

Font styles to use
Serif

```html
<!DOCTYPE html>
<html lang="en">
<head>
<meta charset="utf-8">
<title>My Love for You is… Huge! — Valentine Card</title>
<link rel="stylesheet" href="https://fonts.googleapis.com/css2?family=Dancing+Script:wght@700&family=Open+Sans:wght@700&family=Sniglet:wght@800&display=swap">
<style>
  :root {
    --rose: #fb3d62;
    --rose-light: #ff5a7c;
    --rose-deep: #f02a52;
    --teal-heart: #6fb1c3;
    --aqua: #72cdc8;
    --sky: #5fa6d6;
    --ink: #0d0d0d;
    --paper: #ffffff;
    --skin: #f3a24b;
    --hair: #f0b23c;
    --suit: #2b1a17;
    --heart-pink: #f06b86;
  }
  * { margin: 0; padding: 0; box-sizing: border-box; }
  html, body { width: 847px; height: 1200px; overflow: hidden; background: var(--paper); }
  .card { position: relative; width: 847px; height: 1200px; overflow: hidden; }

  .outside {
    position: absolute; left: 0; top: 0; width: 847px; height: 591px;
    background:
      radial-gradient(ellipse at 30% 20%, var(--rose-deep) 0%, transparent 55%),
      radial-gradient(ellipse at 75% 65%, var(--rose-deep) 0%, transparent 50%),
      radial-gradient(ellipse at 10% 85%, var(--rose-light) 0%, transparent 45%),
      var(--rose);
  }
  .divider { position: absolute; left: 0; top: 591px; width: 847px; height: 3px; background: var(--ink); }

  .heart-title { position: absolute; left: 248px; top: 126px; width: 320px; height: 300px; }
  .heart-title svg { position: absolute; inset: 0; }
  .title-line { position: absolute; color: var(--paper); text-shadow: 2px 3px 4px rgba(0,0,0,0.35); white-space: nowrap; }
  .script { font-family: "Dancing Script", cursive; font-weight: 700; }
  .sans { font-family: "Open Sans", sans-serif; font-weight: 700; }
  .t-my-love { left: -6px; top: 42px; font-size: 82px; line-height: 1; }
  .t-for { left: 26px; top: 148px; font-size: 46px; line-height: 1; }
  .t-you { left: 128px; top: 128px; font-size: 82px; line-height: 1; }
  .t-is { left: 72px; top: 210px; font-size: 46px; line-height: 1; }

  .inside {
    position: absolute; left: 0; top: 594px; width: 847px; height: 606px;
    background:
      radial-gradient(ellipse at 20% 70%, var(--sky) 0%, transparent 55%),
      radial-gradient(ellipse at 85% 30%, #8fd9cf 0%, transparent 50%),
      var(--aqua);
  }

  .figure {
    position: absolute; left: 97px; top: 800px; width: 650px; height: 400px;
    background:
      radial-gradient(ellipse 160px 200px at 50% 45%, var(--skin) 0%, transparent 70%),
      radial-gradient(ellipse 320px 140px at 50% 100%, var(--suit) 0%, transparent 75%),
      radial-gradient(ellipse 140px 160px at 12% 55%, var(--heart-pink) 0%, transparent 70%),
      radial-gradient(ellipse 140px 160px at 88% 55%, var(--heart-pink) 0%, transparent 70%);
  }

  .bubble { position: absolute; left: 42px; top: 622px; width: 759px; height: 270px; }
  .bubble svg { position: absolute; left: 0; top: 0; overflow: visible; }
  .shout {
    position: absolute; left: 36px; top: 12px;
    font-family: "Sniglet", sans-serif; font-weight: 800;
    font-size: 82px; line-height: 86px; color: var(--ink);
    white-space: nowrap;
    transform-origin: left top;
    transform: scaleY(1.3) skewX(-6deg);
  }
</style>
</head>
<body>
<main class="card">
  <section class="outside">
    <div class="heart-title">
      <svg width="320" height="300" viewBox="0 0 335 310" preserveAspectRatio="none" aria-hidden="true">
        <path d="M167 300 C120 255 10 190 10 100 C10 40 55 5 105 5 C140 5 160 25 167 45 C174 25 194 5 229 5 C279 5 325 40 325 100 C325 190 214 255 167 300 Z" fill="var(--teal-heart)"/>
      </svg>
      <span class="title-line script t-my-love">My Love</span>
      <span class="title-line sans t-for">for</span>
      <span class="title-line script t-you">You</span>
      <span class="title-line sans t-is">is...</span>
    </div>
  </section>
  <div class="divider"></div>

  <section class="inside"></section>
  <div class="figure" role="img" aria-label="Cartoon illustration of Harold Benning in a dark suit with arms raised wide, surrounded by small pink hearts"></div>
  <div class="bubble">
    <svg width="759" height="270" viewBox="0 0 759 270" aria-hidden="true">
      <rect x="0" y="0" width="759" height="270" fill="var(--paper)"/>
      <path d="M560 269 L615 269 L600 322 Z" fill="var(--paper)"/>
    </svg>
    <p class="shout">HUUUUUUUUU<br>UUUUUUUUGE!!</p>
  </div>
</main>
</body>
</html>
```